GlintPeach Jewelry Website (zodiac, astrology, angel #s)

website - linkable to Shopify -

similar layout to https://vorlenta.com

similar vibes to https://pexomira.com

-necklaces
-bracelets
-rings
-anklets
-body chains
-earrings
-accessories
-horoscopes

zodiac, astrology, & angel numbers - think masculine meets feminine - spiritual beings

Target Market(s)

spiritual beings who enjoy fun and meaningful jewelry

Industry/Entity Type

Jewelry

Coding

Coded - Design and coding required

Number of Pages Required

5+ page

Colors
59FF00
82FF00
B8FF75
E3FFCB
F4FFEA

Requirements
Must have
• PLEASE VIEW MY BRANDBOOK

```html
<!DOCTYPE html>
<html lang="en">
<head>
<meta charset="utf-8">
<title>GlintPeach Jewelry</title>
<link href="https://fonts.googleapis.com/css2?family=Unbounded:wght@600;800&family=Gilda+Display&family=Montserrat:wght@400;500&display=swap" rel="stylesheet">
<style>
:root{
  --green:#59FF00;
  --green2:#82FF00;
  --mint:#F4FFEA;
  --ink:#1a1a1a;
  --dark:#161616;
  --dark2:#222;
  --grey:#6e6e6e;
  --white:#fff;
}
*{margin:0;padding:0;box-sizing:border-box}
html,body{width:1200px;height:3891px;overflow:hidden}
body{position:relative;background:var(--white);font-family:"Gilda Display",serif;color:var(--ink)}
.abs{position:absolute}
.head{font-family:"Unbounded",sans-serif;font-weight:800;letter-spacing:-1px;text-transform:uppercase}
.topbar{left:0;top:0;width:1200px;height:35px;background:var(--green);font:600 12px "Unbounded",sans-serif;text-align:center;line-height:35px;letter-spacing:.3px}
.header{left:0;top:35px;width:1200px;height:75px;background:var(--white)}
.logo{font-family:"Unbounded",sans-serif;font-weight:800;text-transform:uppercase;letter-spacing:.5px;white-space:nowrap}
.header .logo{left:68px;top:22px;font-size:27px}
.nav{left:369px;top:0;display:flex;height:75px;align-items:center}
.nav a{font:600 13px "Unbounded",sans-serif;color:var(--ink);text-decoration:none;margin-right:37px;position:relative}
.nav a.active{color:var(--green)}
.nav a.active:after{content:"";position:absolute;left:0;right:0;bottom:-28px;height:3px;background:var(--green)}
.hicon{width:32px;height:32px;border-radius:50%;background:#ecffdf;display:flex;align-items:center;justify-content:center}
.hero{left:0;top:110px;width:1200px;height:592px;overflow:hidden;background:radial-gradient(circle at 80% 30%,#f4f4f4 0,#d2d2d2 30%,#8e8e8e 60%,#4d4d4d 100%)}
.hero .model{left:585px;top:0;width:560px;height:592px;background:
  radial-gradient(ellipse 110px 150px at 52% 26%,#b88468 0,#9a6a52 55%,rgba(60,40,30,0) 100%),
  radial-gradient(ellipse 230px 130px at 50% 98%,#151515 0,#1d1d1d 60%,rgba(20,20,20,0) 100%),
  radial-gradient(ellipse 210px 240px at 50% 70%,#c89478 0,#a67458 55%,rgba(120,80,60,0) 100%),
  radial-gradient(ellipse 150px 170px at 45% 22%,#2a1c16 0,#3c2a20 60%,rgba(40,30,20,0) 100%)}
.hero .logo{left:118px;top:216px;font-size:62px;color:var(--white)}
.btn{background:var(--green);border-radius:30px;display:flex;align-items:center;justify-content:center;gap:8px;font:800 12px "Unbounded",sans-serif;text-transform:uppercase;color:var(--ink)}
.shop{left:113px;top:328px;width:169px;height:46px;font-size:15px}
.follow{left:110px;top:533px;display:flex;align-items:center;gap:12px;font:400 13px "Montserrat",sans-serif;color:var(--ink)}
.soc{width:32px;height:32px;border-radius:50%;background:var(--green);display:flex;align-items:center;justify-content:center}
.products-title{top:772px;left:0;width:1200px;text-align:center;font-size:42px}
.intro{left:170px;width:860px;text-align:center;font-size:18px;line-height:27px;color:#333}
.card{width:282px}
.card .ph{width:282px;height:293px;border:1px solid #333}
.card .stars{margin-top:20px;text-align:center;height:18px}
.card h3{margin-top:6px;text-align:center;font:800 17px "Unbounded",sans-serif;text-transform:uppercase;letter-spacing:-.3px;white-space:nowrap}
.card .price{margin-top:8px;text-align:center;font-size:30px}
.card .btn{margin:10px auto 0;width:143px;height:37px;font-size:10px}
.about-band{left:524px;top:1449px;width:676px;height:561px;background:var(--green)}
.about-ph{left:110px;top:1514px;width:491px;height:431px;background:
  radial-gradient(ellipse 120px 110px at 55% 28%,#d1a083 0,#b47f62 55%,rgba(150,110,80,0) 100%),
  radial-gradient(ellipse 190px 120px at 50% 100%,#111 0,#1b1b1b 60%,rgba(20,20,20,0) 100%),
  radial-gradient(ellipse 200px 150px at 50% 68%,#c8977a 0,#a77a5d 55%,rgba(120,90,60,0) 100%),
  linear-gradient(135deg,#c9b98a,#7d7a4e 45%,#3d4030)}
.about-title{left:634px;top:1524px;font-size:42px}
.about-text{left:634px;top:1581px;width:452px;font-size:15.6px;line-height:24.8px;text-align:justify}
.learn{left:628px;top:1883px;width:185px;height:46px;background:var(--ink);color:var(--green);font-size:14px}
.acc-bg{left:0;top:2010px;width:1200px;height:750px;background:var(--mint)}
.testi-title{left:0;top:2836px;width:1200px;text-align:center;font-size:42px}
.quote{left:131px;top:2940px;width:473px;font-style:italic;font-size:16.5px;line-height:25px;text-align:justify}
.tname{left:129px;top:3110px;font:800 24px "Unbounded",sans-serif;letter-spacing:-.5px}
.trole{left:129px;top:3146px;font-style:italic;font-size:15px;color:#555}
.tframe{left:652px;top:2917px;width:404px;height:302px;border:4px solid var(--green);background:
  radial-gradient(ellipse 70px 90px at 38% 30%,#d9ad94 0,#c08f74 55%,rgba(190,150,120,0) 100%),
  radial-gradient(ellipse 140px 110px at 55% 92%,#1c1c1c 0,#2c2c2c 60%,rgba(30,30,30,0) 100%),
  radial-gradient(ellipse 80px 110px at 33% 22%,#1c1410 0,#2a1e18 60%,rgba(30,20,15,0) 100%),
  linear-gradient(135deg,#f4f4f4,#dcdcdc 60%,#a8a8a8)}
.news-grey{left:0;top:3306px;width:1200px;height:144px;background:var(--grey)}
.news-green{left:0;top:3306px;width:539px;height:144px;background:var(--green);clip-path:polygon(0 0,100% 0,87.5% 100%,0 100%)}
.news-title{left:116px;top:3340px;font-size:40px}
.news-sub{left:116px;top:3393px;width:340px;font-style:italic;font-size:11.5px;line-height:16px}
.news-form{left:552px;top:3362px;width:536px;height:62px;background:var(--white);display:flex;align-items:center;padding:0 8px 0 18px}
.news-form span{flex:1;font:400 14px "Montserrat",sans-serif;color:#888;margin-left:12px}
.submit{width:129px;height:47px;background:var(--green);font:800 16px "Unbounded",sans-serif;display:flex;align-items:center;justify-content:center}
.footer{left:0;top:3450px;width:1200px;height:368px;background:var(--dark)}
.footer .logo{left:110px;top:172px;font-size:29px;color:var(--white);width:252px;text-align:center}
.fsoc{left:175px;top:244px;display:flex;gap:12px}
.fsoc .soc{background:#3a3a3a}
.fcol h4{font:800 18px "Unbounded",sans-serif;color:var(--white);text-transform:uppercase;letter-spacing:-.3px}
.fcol h4:after{content:"";display:block;width:46px;height:4px;background:var(--green);margin-top:8px}
.fcol ul{list-style:none;margin-top:24px}
.fcol li{font-size:12.5px;color:var(--white);height:25.7px}
.fcol li:before{content:"»";color:var(--green);margin-right:6px;font-size:15px}
.citem{display:flex;gap:18px;margin-bottom:22px}
.cicon{width:34px;height:34px;border-radius:50%;background:#2c2c2c;display:flex;align-items:center;justify-content:center;flex:none}
.citem small{display:block;font-size:12px;color:#bbb}
.citem p{font-family:"Montserrat",sans-serif;font-size:12.5px;color:var(--white);line-height:19px;font-weight:500}
.bottom{left:0;top:3818px;width:1200px;height:73px;background:var(--dark2);text-align:center;line-height:73px;font:400 14px "Montserrat",sans-serif;color:var(--white)}
.totop{left:1114px;top:3795px;width:42px;height:38px;background:var(--green);border-radius:6px;display:flex;align-items:center;justify-content:center}
</style>
</head>
<body>
<svg width="0" height="0" style="position:absolute"><defs>
<symbol id="star" viewBox="0 0 20 20"><path d="M10 1l2.8 6 6.2.6-4.7 4.2 1.4 6.2L10 14.8 4.3 18l1.4-6.2L1 7.6l6.2-.6z" fill="#59FF00"/></symbol>
<symbol id="i-heart" viewBox="0 0 16 16"><path d="M8 14S1.5 9.8 1.5 5.5A3.3 3.3 0 0 1 8 4a3.3 3.3 0 0 1 6.5 1.5C14.5 9.8 8 14 8 14z" fill="currentColor"/></symbol>
<symbol id="i-link" viewBox="0 0 16 16"><path d="M6.5 9.5l3-3M7 4.5l1.2-1.2a2.6 2.6 0 0 1 3.7 3.7L10.7 8.2M9 11.5l-1.2 1.2a2.6 2.6 0 0 1-3.7-3.7L5.3 7.8" fill="none" stroke="currentColor" stroke-width="1.8" stroke-linecap="round"/></symbol>
<symbol id="i-mail" viewBox="0 0 16 16"><rect x="1.5" y="3.5" width="13" height="9" rx="1.5" fill="none" stroke="currentColor" stroke-width="1.6"/><path d="M2 4.5l6 4.5 6-4.5" fill="none" stroke="currentColor" stroke-width="1.6"/></symbol>
</defs></svg>

<div class="abs topbar">GET FREE SHIPPING ON ORDER $50+</div>

<header class="abs header">
  <div class="abs logo">GlintPeach</div>
  <nav class="abs nav">
    <a class="active">Home</a><a>About</a><a>Products</a><a>Accessories</a><a>More</a><a>Wholesale</a><a style="margin-right:12px">Contact</a>
    <span style="width:1px;height:30px;background:#bbb;margin-right:12px"></span>
    <div class="hicon" style="margin-right:12px"><svg width="14" height="14" viewBox="0 0 14 14"><circle cx="6" cy="6" r="4.5" fill="none" stroke="#111" stroke-width="2"/><path d="M9.3 9.3L13 13" stroke="#111" stroke-width="2"/></svg></div>
    <div class="hicon"><svg width="14" height="16" viewBox="0 0 14 16"><rect x="1.5" y="5" width="11" height="10" rx="1.5" fill="none" stroke="#111" stroke-width="1.6"/><path d="M4.5 5V3.5a2.5 2.5 0 0 1 5 0V5" fill="none" stroke="#111" stroke-width="1.6"/></svg></div>
  </nav>
</header>

<section class="abs hero">
  <div class="abs model" role="img" aria-label="Model wearing a colourful pendant necklace, earrings and bangle"></div>
  <svg class="abs" style="left:44px;top:272px" width="24" height="48" viewBox="0 0 24 48"><path d="M22 2L2 24l20 22" fill="none" stroke="#fff" stroke-width="2"/></svg>
  <svg class="abs" style="left:1132px;top:272px" width="24" height="48" viewBox="0 0 24 48"><path d="M2 2l20 22L2 46" fill="none" stroke="#fff" stroke-width="2"/></svg>
  <div class="abs logo">GlintPeach</div>
  <div class="abs btn shop">Shop Now <svg width="8" height="10" viewBox="0 0 8 10"><path d="M2 1l4 4-4 4" fill="none" stroke="#111" stroke-width="2"/></svg></div>
  <div class="abs follow">Follow Us:
    <div class="soc" style="color:#111"><svg width="14" height="14"><use href="#i-heart"/></svg></div>
    <div class="soc" style="color:#111"><svg width="14" height="14"><use href="#i-link"/></svg></div>
    <div class="soc" style="color:#111"><svg width="14" height="14"><use href="#i-mail"/></svg></div>
  </div>
  <svg class="abs" style="left:590px;top:540px" width="20" height="120" viewBox="0 0 20 120"><rect x="2" y="2" width="16" height="28" rx="8" fill="none" stroke="#59FF00" stroke-width="2"/><path d="M10 8v7" stroke="#59FF00" stroke-width="2"/><path d="M10 30v90" stroke="#59FF00" stroke-width="1"/></svg>
</section>

<h2 class="abs head products-title">Our Products</h2>
<p class="abs intro" style="top:820px">Dseste natus error sit voluptatem accusan tium doloremque laudantium, totam rem aperiam, ease aque ipaefdsa quae ab illo inventore veritatis ease quasi architecto.</p>

<div class="abs card" style="left:110px;top:913px"><div class="ph" role="img" aria-label="Teardrop crystal pendant necklace on dark wet stone" style="background:radial-gradient(ellipse 70px 90px at 52% 62%,#6f8fb0 0,#3f5873 50%,rgba(40,50,60,0) 100%),radial-gradient(circle at 30% 20%,#9aa0a5 0,rgba(90,95,100,0) 45%),linear-gradient(135deg,#5d6368,#2c3035 55%,#121417)"></div><div class="stars"><svg width="100" height="18"><use href="#star" width="18" height="18"/><use href="#star" x="20" width="18" height="18"/><use href="#star" x="40" width="18" height="18"/><use href="#star" x="60" width="18" height="18"/><use href="#star" x="80" width="18" height="18"/></svg></div><h3>Crystal Drip Necklace</h3><div class="price">$ 40.00</div><div class="btn">Add to cart <svg width="6" height="8" viewBox="0 0 6 8"><path d="M1 1l3 3-3 3" fill="none" stroke="#111" stroke-width="1.5"/></svg></div></div>
<div class="abs card" style="left:459px;top:913px"><div class="ph" role="img" aria-label="Woman wearing a colourful jewelled statement necklace" style="background:radial-gradient(ellipse 130px 60px at 50% 42%,#3c5ea8 0,#6d74b8 40%,rgba(200,160,140,0) 100%),radial-gradient(ellipse 160px 90px at 50% 100%,#1c1c1c 0,rgba(30,30,30,0) 100%),linear-gradient(180deg,#4a3a30,#d2a88e 35%,#c9987c 75%,#2b2b2b)"></div><div class="stars"><svg width="100" height="18"><use href="#star" width="18" height="18"/><use href="#star" x="20" width="18" height="18"/><use href="#star" x="40" width="18" height="18"/><use href="#star" x="60" width="18" height="18"/><use href="#star" x="80" width="18" height="18"/></svg></div><h3>Crystal Drip Bracelets</h3><div class="price">$ 40.00</div><div class="btn">Add to cart <svg width="6" height="8" viewBox="0 0 6 8"><path d="M1 1l3 3-3 3" fill="none" stroke="#111" stroke-width="1.5"/></svg></div></div>
<div class="abs card" style="left:806px;top:913px"><div class="ph" role="img" aria-label="Woman with long hair wearing fan-shaped earrings" style="background:radial-gradient(ellipse 90px 120px at 45% 40%,#c99878 0,#b07d5c 55%,rgba(110,70,45,0) 100%),radial-gradient(ellipse 150px 80px at 50% 100%,#3c5070 0,rgba(60,80,110,0) 100%),linear-gradient(135deg,#4e3422,#7a5436 50%,#3a2a20)"></div><div class="stars"><svg width="100" height="18"><use href="#star" width="18" height="18"/><use href="#star" x="20" width="18" height="18"/><use href="#star" x="40" width="18" height="18"/><use href="#star" x="60" width="18" height="18"/><use href="#star" x="80" width="18" height="18"/></svg></div><h3>Crystal Drip Rings</h3><div class="price">$ 40.00</div><div class="btn">Add to cart <svg width="6" height="8" viewBox="0 0 6 8"><path d="M1 1l3 3-3 3" fill="none" stroke="#111" stroke-width="1.5"/></svg></div></div>

<div class="abs about-band"></div>
<div class="abs about-ph" role="img" aria-label="Woman in a black strapless dress wearing long drop earrings and a bracelet"></div>
<h2 class="abs head about-title">About Us</h2>
<div class="abs about-text">
  <p>Saerspiciatis undeasepklsaoiise osamnis istasesee njhhjkatus error silksdoiseklt voluptatem accusan tium doloreasmque laudantium, totam rem aperiam, ease aque ipaefdsa quae ab illo inventore veritatis eklsdoase quasi architecto beatae vitae diascta sunt explicabo. Nemo enim ipsam voluptatem quia volupta sde sessitasese aspernatur autodit aut fugitsdsed quia conseq aauuntur magni dolores eos qui ratione.</p>
  <p style="margin-top:22px">Dseste natus error sit voluptatem accusan tium doloremque laudantium, totam rem aperiam, ease aque ipaefdsa quae ab illo inventore veritatis ease quasi architecto.</p>
</div>
<div class="abs btn learn">Learn More <svg width="8" height="10" viewBox="0 0 8 10"><path d="M2 1l4 4-4 4" fill="none" stroke="#59FF00" stroke-width="2"/></svg></div>

<div class="abs acc-bg"></div>
<h2 class="abs head products-title" style="top:2086px">Accessories</h2>
<p class="abs intro" style="top:2134px">Dseste natus error sit voluptatem accusan tium doloremque laudantium, totam rem aperiam, ease aque ipaefdsa quae ab illo inventore veritatis ease quasi architecto.</p>

<div class="abs card" style="left:110px;top:2227px"><div class="ph" role="img" aria-label="Blonde woman in a checked blazer with a gold chain, city street behind" style="background:radial-gradient(ellipse 60px 70px at 50% 22%,#e4cfa6 0,#d9b98e 55%,rgba(200,170,130,0) 100%),radial-gradient(ellipse 110px 150px at 50% 78%,#f2f0ea 0,#5d5a60 45%,rgba(80,80,90,0) 100%),linear-gradient(135deg,#d8c2a4,#a8785a 50%,#6e5a50)"></div><div class="stars"><svg width="100" height="18"><use href="#star" width="18" height="18"/><use href="#star" x="20" width="18" height="18"/><use href="#star" x="40" width="18" height="18"/><use href="#star" x="60" width="18" height="18"/><use href="#star" x="80" width="18" height="18"/></svg></div><h3>Crystal Drip Anklets</h3><div class="price">$ 40.00</div><div class="btn">Add to cart <svg width="6" height="8" viewBox="0 0 6 8"><path d="M1 1l3 3-3 3" fill="none" stroke="#111" stroke-width="1.5"/></svg></div></div>
<div class="abs card" style="left:459px;top:2227px"><div class="ph" role="img" aria-label="Woman in a rust skirt holding a white crochet bag on a wooden bench" style="background:radial-gradient(ellipse 55px 80px at 50% 62%,#efe9de 0,#d8d0c2 55%,rgba(220,210,190,0) 100%),radial-gradient(ellipse 120px 180px at 50% 85%,#b2532f 0,#8e3f24 55%,rgba(140,60,35,0) 100%),linear-gradient(180deg,#d4b4a0,#6e5c4e 35%,#8a8378)"></div><div class="stars"><svg width="100" height="18"><use href="#star" width="18" height="18"/><use href="#star" x="20" width="18" height="18"/><use href="#star" x="40" width="18" height="18"/><use href="#star" x="60" width="18" height="18"/><use href="#star" x="80" width="18" height="18"/></svg></div><h3>Crystal Drip Body Chains</h3><div class="price">$ 40.00</div><div class="btn">Add to cart <svg width="6" height="8" viewBox="0 0 6 8"><path d="M1 1l3 3-3 3" fill="none" stroke="#111" stroke-width="1.5"/></svg></div></div>
<div class="abs card" style="left:806px;top:2227px"><div class="ph" role="img" aria-label="Woman in a blue top with a fringed bag and pendant necklace" style="background:radial-gradient(ellipse 90px 130px at 40% 80%,#a36a3a 0,#7e4e28 55%,rgba(120,80,40,0) 100%),radial-gradient(ellipse 130px 140px at 60% 45%,#8fa5ba 0,#6f869c 55%,rgba(100,120,140,0) 100%),linear-gradient(135deg,#e8dcc4,#c8b8a0 50%,#6a7a86)"></div><div class="stars"><svg width="100" height="18"><use href="#star" width="18" height="18"/><use href="#star" x="20" width="18" height="18"/><use href="#star" x="40" width="18" height="18"/><use href="#star" x="60" width="18" height="18"/><use href="#star" x="80" width="18" height="18"/></svg></div><h3>Crystal Drip Earrings</h3><div class="price">$ 40.00</div><div class="btn">Add to cart <svg width="6" height="8" viewBox="0 0 6 8"><path d="M1 1l3 3-3 3" fill="none" stroke="#111" stroke-width="1.5"/></svg></div></div>

<h2 class="abs head testi-title">Testimonials</h2>
<p class="abs quote">“Saerspiciatis undeasepoiise osamnis istasesee njhhjkatus error sit voluptatem accusan tium doloreasmque laudantium, totam rem aperiam, ease aque ipaefdsa quae ab illo inventore veritatis ease quasi architecto beatae vitae diascta sunt explicabo. Nemo enim ipsam voluptatem quia volupta sde sessitasese aspernatur autodit aut fugitsdsed quia conseq.”</p>
<div class="abs tname">Marina Holt</div>
<div class="abs trole">Loyal Client</div>
<svg class="abs" style="left:129px;top:3172px" width="100" height="18"><use href="#star" width="18" height="18"/><use href="#star" x="20" width="18" height="18"/><use href="#star" x="40" width="18" height="18"/><use href="#star" x="60" width="18" height="18"/><use href="#star" x="80" width="18" height="18"/></svg>
<svg class="abs" style="left:533px;top:3140px" width="16" height="28" viewBox="0 0 16 28"><path d="M14 2L2 14l12 12" fill="none" stroke="#111" stroke-width="1.6"/></svg>
<svg class="abs" style="left:587px;top:3140px" width="16" height="28" viewBox="0 0 16 28"><path d="M2 2l12 12L2 26" fill="none" stroke="#111" stroke-width="1.6"/></svg>
<div class="abs tframe" role="img" aria-label="Woman in a black leather top wearing statement earrings and rings"></div>

<div class="abs news-grey"></div>
<div class="abs news-green"></div>
<h2 class="abs head news-title">Newsletter</h2>
<p class="abs news-sub">Sersplciatis unde omnis iste natus error sit voluptatem accusantium doloremque laudantium.</p>
<div class="abs news-form">
  <svg width="24" height="16" viewBox="0 0 24 16"><rect width="24" height="16" rx="2" fill="#ccc"/><path d="M1 1l11 8 11-8" fill="none" stroke="#fff" stroke-width="1.5"/></svg>
  <span>Email Address</span>
  <div class="submit">SUBMIT</div>
</div>

<footer class="abs footer">
  <div class="abs logo">GlintPeach</div>
  <div class="abs fsoc">
    <div class="soc" style="color:#fff"><svg width="14" height="14"><use href="#i-heart"/></svg></div>
    <div class="soc" style="color:#fff"><svg width="14" height="14"><use href="#i-link"/></svg></div>
    <div class="soc" style="color:#fff"><svg width="14" height="14"><use href="#i-mail"/></svg></div>
  </div>
  <div class="abs fcol" style="left:424px;top:83px">
    <h4>Quick Links</h4>
    <ul><li>Home</li><li>About</li><li>Products</li><li>Accessories</li><li>More</li><li>Wholesale</li><li>Contact</li></ul>
  </div>
  <div class="abs fcol" style="left:644px;top:83px">
    <h4>Links</h4>
    <ul><li>Terms Of Use</li><li>Track Orders</li><li>Shipping</li><li>Cancellation</li><li>Returns</li><li>Careers</li><li>Site Map</li></ul>
  </div>
  <div class="abs fcol" style="left:839px;top:83px">
    <h4>Contact Us</h4>
    <div style="margin-top:26px">
      <div class="citem"><div class="cicon"><svg width="14" height="18" viewBox="0 0 14 18"><path d="M7 1a6 6 0 0 1 6 6c0 4.5-6 10-6 10S1 11.5 1 7a6 6 0 0 1 6-6z" fill="#59FF00"/><circle cx="7" cy="7" r="2.2" fill="#2c2c2c"/></svg></div><div><small>Address</small><p>42 Linden Row, Harbourview,<br>Canada, 20417</p></div></div>
      <div class="citem"><div class="cicon"><svg width="16" height="16" viewBox="0 0 16 16"><path d="M3 1l3 3-2 2c1 2.5 3.5 5 6 6l2-2 3 3-2 2C7 15 1 9 1 3z" fill="#59FF00"/></svg></div><div><small>Call Us</small><p>+1 (555) 214-7730</p></div></div>
      <div class="citem"><div class="cicon"><svg width="16" height="12" viewBox="0 0 16 12"><rect width="16" height="12" rx="1.5" fill="#59FF00"/><path d="M1 1l7 5 7-5" fill="none" stroke="#2c2c2c" stroke-width="1.4"/></svg></div><div><small>Email</small><p>info@glintpeach.com</p></div></div>
    </div>
  </div>
</footer>
<div class="abs bottom">©2023. All rights reserved.</div>
<div class="abs totop"><svg width="12" height="8" viewBox="0 0 12 8"><path d="M1 7l5-5 5 5" fill="none" stroke="#111" stroke-width="2"/></svg></div>
</body>
</html>
```